Web Page for marketing online agency

We are an online marketing agency that is acing the direct response model. We engage with our customers throughout different marketing techniques as research copy-writing, advertisements and content writing. We would need a website design that will have four main aspects: The Vision; stating who we are, The Mission; stating what we do, The Team And It's Values, and a Contact Form. For this design we would want a sharp, clean and smart approach, with illustrated elements or suggestive images. You can use the attached copy, the logo, the USP and the motto. Please integrate them as you see fit while keeping in mind the previous needs and copy. This website is going to be our connection with our possible partners, future colleagues and even our clients. You may submit a design for one page or integrate the 4 different aspects on separate web pages.
Target Market(s)
business partners, future employees, age range 25-60
Industry/Entity Type
Direct Marketing
Number of Pages Required
1 page
Requirements
Must have
- Menu / Header
- 4 Parts or 4 Pages including: vision, mission, team, contact
- Logo
- Motto: Direct Brilliance
- USP: We help people help themselves.
- The copy attached
Nice to have
- Representative illustrated images or elements
Should not have
- A boring design, classical design - WordPress like

```html
<!DOCTYPE html>
<html lang="en">
<head>
<meta charset="utf-8">
<title>NovaKin – Direct Brilliance</title>
<link href="https://fonts.googleapis.com/css2?family=Montserrat:wght@400;500;600;700&display=swap" rel="stylesheet">
<style>
:root{
  --blue:#2a9fd8;
  --blue-soft:#a9d8f1;
  --ink:#222;
  --text:#333;
  --grey-band:#efefef;
  --white:#fff;
}
*{box-sizing:border-box;margin:0;padding:0}
html,body{width:1200px;height:2378px;overflow:hidden}
body{position:relative;font-family:'Montserrat',sans-serif;color:var(--text);background:var(--white)}
.abs{position:absolute}

/* header */
.site-header{left:0;top:0;width:1200px;height:73px;background:var(--white);z-index:5}
.brand{left:150px;top:16px;display:flex;align-items:center;gap:8px;font-size:30px;font-weight:600;color:var(--ink)}
.brand-dot{width:22px;height:22px;border-radius:50%;background:var(--blue)}
.main-nav a{position:absolute;top:37px;font-size:13px;font-weight:600;color:var(--ink);text-decoration:none;letter-spacing:.3px}
.btn{display:flex;align-items:center;justify-content:center;background:var(--blue);color:var(--white);font-weight:700;border-radius:18px;text-decoration:none;font-size:13px}
.nav-contact{left:937px;top:30px;width:114px;height:32px}

/* hero */
.hero-photo{left:0;top:73px;width:1200px;height:470px;background:linear-gradient(135deg,#5a4a3e 0%,#8b7b6c 30%,#c9c2b8 55%,#6f6a66 80%,#3b3631 100%)}
.hero-wave{left:0;top:420px;width:1200px;height:130px}
.hero-box{left:150px;top:197px;width:600px;height:144px;background:rgba(255,255,255,.72)}
.hero-title{left:166px;top:198px;font-size:29px;font-weight:700;color:var(--ink);line-height:44px;text-transform:uppercase;letter-spacing:-.4px}
.hero-title span{display:block}
.hero-cta{left:166px;top:298px;width:111px;height:30px}

/* section headings */
.section-title{width:1200px;left:0;text-align:center;font-size:22px;font-weight:700;color:var(--ink);letter-spacing:.3px}
.title-rule{width:72px;height:2px;background:var(--blue-soft);left:564px}

/* vision */
.vision-bubble{border-radius:50%;background:var(--blue-soft);opacity:.75}
.vision-block{left:150px;top:644px;width:600px;display:flex;flex-direction:column}
.vision-copy{font-size:11.8px;line-height:18px;color:var(--text)}
.vision-copy .lead{font-size:14.4px;line-height:19px;color:var(--ink);margin-bottom:8px;letter-spacing:-.1px}
.vision-copy p{margin-bottom:7px}
.values-title{margin-top:10px;text-align:center;font-size:14px;font-weight:600;color:var(--ink)}
.values-list{margin-top:10px;display:flex;gap:24px;font-size:13px;color:var(--ink)}
.values-list li{list-style:none;display:flex;align-items:center;gap:7px;white-space:nowrap}
.values-list svg{width:28px;height:26px}

/* mission */
.mission-band{left:0;top:1073px;width:1200px;height:309px;background:var(--grey-band)}
.mission-intro{left:0;width:1200px;top:1177px;text-align:center;font-size:15px;line-height:19px;color:var(--ink)}
.mission-item{width:190px;text-align:center;font-size:13px;line-height:18px;color:var(--ink)}
.mission-item svg{display:block;margin:0 auto 17px;width:40px;height:40px}

/* team */
.team-intro{left:0;width:1200px;top:1472px;text-align:center;font-size:13px;line-height:18px;color:var(--ink)}
.member-photo{border-radius:50%;background:radial-gradient(circle at 50% 45%,#b89a86 0%,#7c6a5e 45%,#2e2a28 100%)}
.member-photo.light{background:radial-gradient(circle at 50% 45%,#d8c4b4 0%,#c7c7c7 50%,#f2f2f2 100%)}
.name-bubble{border-radius:50%;background:var(--blue-soft);display:flex;flex-direction:column;align-items:center;justify-content:center;text-align:center;font-size:9px;line-height:11px;color:var(--ink)}
.name-bubble b{font-weight:700}
.dot-bubble{border-radius:50%;background:var(--blue-soft)}
.member-copy{font-size:11.6px;line-height:18px;color:var(--text)}
.member-copy p{margin-bottom:9px}
.member-copy strong{color:var(--ink)}

/* contact */
.contact-photo{left:0;top:1934px;width:1200px;height:400px;background:linear-gradient(120deg,#8f8a80 0%,#d7d3cc 35%,#efece7 60%,#b6b1a8 100%)}
.contact-wave{left:0;top:1920px;width:1200px;height:90px}
.field-label{left:150px;font-size:13px;color:var(--ink)}
.field{background:var(--white);border:1px solid #ddd;font-size:12.5px;color:#aaa;padding:0 12px;display:flex;align-items:center}
.field.area{align-items:flex-start;padding-top:10px}
.send-btn{left:558px;top:2260px;width:141px;height:29px;font-size:14px;border-radius:16px}
.map{left:729px;top:2099px;width:322px;height:190px;background:linear-gradient(150deg,#e6e3dc 0%,#d8e6cf 45%,#f0ede6 70%,#c9dfe8 100%)}

/* footer */
.site-footer{left:0;top:2327px;width:1200px;height:51px;background:var(--blue)}
.copyright{left:150px;top:2346px;font-size:11px;color:var(--white)}
.social{top:2342px;width:20px;height:20px;border-radius:50%;background:var(--white)}
</style>
</head>
<body>

<header class="abs site-header">
  <div class="abs brand"><span>NovaKin</span><span class="brand-dot"></span></div>
  <nav class="main-nav">
    <a style="left:436px">OUR VISION</a>
    <a style="left:562px">OUR MISSION</a>
    <a style="left:699px">OUR TEAM</a>
    <a style="left:818px">PARTNERS</a>
  </nav>
  <a class="abs btn nav-contact">CONTACT US</a>
</header>

<div class="abs hero-photo" role="img" aria-label="Photo of a team working at a desk with laptops, notebooks and coffee"></div>
<svg class="abs hero-wave" viewBox="0 0 1200 130" preserveAspectRatio="none">
  <path d="M0 55 C220 130 420 115 640 95 C860 75 1020 70 1200 90 L1200 130 L0 130 Z" fill="#fff"/>
</svg>
<div class="abs hero-box"></div>
<h1 class="abs hero-title"><span>“Direct Brilliance”</span><span>We help people help themselves</span></h1>
<a class="abs btn hero-cta">CONTACT US</a>

<div class="abs vision-bubble" style="left:734px;top:594px;width:316px;height:206px"></div>
<div class="abs vision-bubble" style="left:747px;top:825px;width:132px;height:132px"></div>
<div class="abs vision-bubble" style="left:693px;top:960px;width:72px;height:66px"></div>

<h2 class="abs section-title" style="top:586px">OUR VISION</h2>
<div class="abs title-rule" style="top:625px"></div>

<div class="abs vision-block">
  <div class="vision-copy">
    <p class="lead">We are a direct response company that creates and sells information products and services that millions of people find interesting and important in their lives.</p>
    <p>We are specialized in the self-reliance market and we serve conservative Americans. We are in this business to serve globally and to grow individually.</p>
    <p>What we serve and inspire are people who need safety, comfort and peace of mind. We deliver empowerment through products that create fertile shortcuts to solutions, disentangle reality, simplify choices and ultimately make lives better. We give reassurance and confidence to these people through fresh, unique solutions.</p>
    <p>We get our inspiration from modern heroes and make their stories available for others.In a way we are democratizing wisdom because we solve serious problems shared by millions of people worldwide. We might not directly save lives, but we try to make a change. We help people help themselves. With our thirst for knowledge and drive for constant improvement, we know we'll find a solution to any challenge. And while doing that, we decided to water our inner seeds and harvest the best of our humanity.</p>
    <p>We invest time and energy in becoming better in the competition with ourselves. We believe that our better selves of tomorrow will nurture better tomorrows for others.</p>
  </div>
  <div class="values-title">Values:</div>
  <ul class="values-list">
    <li><svg viewBox="0 0 28 26" fill="none" stroke="#2a9fd8" stroke-width="1.4"><path d="M2 9 L8 7 L14 12 L20 7 L26 9 M5 10 L11 18 Q13 20 15 18 L22 11"/></svg>Fairness</li>
    <li><svg viewBox="0 0 28 26" fill="none" stroke="#2a9fd8" stroke-width="1.4"><path d="M14 10 C10 6 6 9 10 13 L14 16 L18 13 C22 9 18 6 14 10 Z M3 18 L10 22 L24 18"/></svg>Caring</li>
    <li><svg viewBox="0 0 28 26" fill="none" stroke="#2a9fd8" stroke-width="1.4"><path d="M14 2 L24 6 L23 14 Q20 21 14 24 Q8 21 5 14 L4 6 Z M10 13 L13 16 L18 10"/></svg>Safety</li>
    <li><svg viewBox="0 0 28 26" fill="none" stroke="#2a9fd8" stroke-width="1.4"><path d="M3 20 Q10 18 14 10 L25 4 L18 14 Q14 22 3 20 Z"/></svg>Freedom</li>
    <li><svg viewBox="0 0 28 26" fill="none" stroke="#2a9fd8" stroke-width="1.4"><circle cx="14" cy="6" r="3.5"/><path d="M8 15 Q14 10 20 15 M3 18 L11 23 L25 18"/></svg>Unconditioned help</li>
  </ul>
</div>

<div class="abs mission-band"></div>
<h2 class="abs section-title" style="top:1120px">OUR MISSION</h2>
<div class="abs title-rule" style="top:1159px"></div>
<p class="abs mission-intro">We are masters of direct response marketing.<br>We create content and build solutions to profound challenges for millions of people.</p>

<div class="abs mission-item" style="left:273px;top:1244px">
  <svg viewBox="0 0 40 40"><circle cx="20" cy="16" r="11" fill="#2a9fd8"/><rect x="15" y="27" width="10" height="7" rx="2" fill="#2a9fd8"/><circle cx="20" cy="16" r="4" fill="none" stroke="#fff" stroke-width="2"/></svg>
  Create and aggregate great information product
</div>
<div class="abs mission-item" style="left:495px;top:1244px">
  <svg viewBox="0 0 40 40"><path d="M9 6 L14 3 L26 26 L22 30 Z" fill="#2a9fd8"/><path d="M22 30 L26 26 L25 33 Z" fill="#2a9fd8"/><path d="M24 36 Q30 30 32 34 Q34 38 38 32" fill="none" stroke="#2a9fd8" stroke-width="1.5"/></svg>
  Write content that compels people to act
</div>
<div class="abs mission-item" style="left:737px;top:1244px">
  <svg viewBox="0 0 40 40"><circle cx="27" cy="11" r="8" fill="none" stroke="#2a9fd8" stroke-width="2"/><path d="M21 17 L16 22" stroke="#2a9fd8" stroke-width="3"/><path d="M4 26 Q10 20 18 24 L22 30 Q18 36 8 36 Z" fill="#2a9fd8"/></svg>
  Deep research to offer simple quick and easy solutions
</div>

<h2 class="abs section-title" style="top:1415px">OUR TEAM &amp; VALUES</h2>
<div class="abs title-rule" style="top:1454px"></div>
<p class="abs team-intro">We're a small team of smart, funny hard-working specialists who are pushing to become the #1 company in self-reliance. High<br>ambition, radical honesty and a result-oriented mindset are encouraged at NovaKin.</p>

<div class="abs member-photo light" style="left:170px;top:1534px;width:168px;height:120px" role="img" aria-label="Portrait of Dorian Vale, CEO"></div>
<div class="abs name-bubble" style="left:176px;top:1657px;width:74px;height:74px"><b>Dorian Vale,</b>CEO NovaKin</div>
<div class="abs dot-bubble" style="left:147px;top:1726px;width:38px;height:32px"></div>

<div class="abs member-copy" style="left:404px;top:1532px;width:636px">
  <p>Dorian started or was involved in 15 failed businesses before discovering online copywriting. After that, he ended up writing for Orbix Inc. and did 10-12 "successful" projects there, at least 3 of which broke the million-dollar mark. He wrote the famous HomeGridPower, and the infamous VoltSecret and Harlan Motor sales letters.</p>
  <p>In 2012 Dorian decided to start his own business, and to sell legit products he and his team could actually be proud of. Six months into the business they had Garden Freedom, a legendary aquaponics/survival food offer that did over 150,000 initial sales. Ever since, they've been doing successful survival offers, and are one of the few "survival" players constantly coming up with new offers.</p>
  <p><strong>Key personal strengths</strong>: copywriting, consulting, positioning, idea generation, mentoring.</p>
</div>

<div class="abs member-copy" style="left:147px;top:1792px;width:665px">
  <p>Since the company's late 2012 start, Marco grew a network of 5000 affiliates, that dominates ClickMarket's survival niche - 3 out of top 5 products are NovaKin offers, under the Survivalwise brand.</p>
  <p>He currently oversees sales of $10 million / year, management of a 160k+ email list, marketing, business development and human resources for both the local NovaKin team and the international one.</p>
  <p><strong>Key personal strengths</strong>: strong networking skills, sales, risk management, leadership.</p>
</div>

<div class="abs member-photo" style="left:878px;top:1742px;width:172px;height:114px" role="img" aria-label="Portrait of Marco Vale, co-founder and affiliate manager"></div>
<div class="abs name-bubble" style="left:884px;top:1856px;width:76px;height:76px"><b>Marco Vale,</b>Cofounder &amp;<br>Affiliate Manager<br>NovaKin</div>
<div class="abs dot-bubble" style="left:855px;top:1928px;width:40px;height:32px"></div>

<div class="abs contact-photo" role="img" aria-label="Soft-focus photo of a laptop and plants on a bright desk"></div>
<svg class="abs contact-wave" viewBox="0 0 1200 90" preserveAspectRatio="none">
  <path d="M0 0 L1200 0 L1200 40 C1000 5 760 8 560 35 C360 62 160 60 0 30 Z" fill="#fff"/>
</svg>

<h2 class="abs section-title" style="top:2035px">CONTACT US</h2>
<div class="abs title-rule" style="top:2073px"></div>

<div class="abs field-label" style="top:2079px">*Name:</div>
<div class="abs field" style="left:150px;top:2099px;width:227px;height:31px">Write full name</div>
<div class="abs field-label" style="top:2136px">*Email:</div>
<div class="abs field" style="left:150px;top:2156px;width:227px;height:31px">Write email adress</div>
<div class="abs field-label" style="top:2193px">Website:</div>
<div class="abs field" style="left:150px;top:2214px;width:227px;height:31px">Write website adress</div>

<div class="abs field-label" style="left:398px;top:2079px">Message:</div>
<div class="abs field area" style="left:398px;top:2099px;width:303px;height:146px">Write your message</div>
<a class="abs btn send-btn">SEND MESSAGE</a>

<div class="abs map" role="img" aria-label="Street map showing the office location"></div>

<footer class="abs site-footer"></footer>
<div class="abs copyright">Copyright @ 2018 NovaKin. All rights reserved.</div>
<div class="abs social" style="left:977px" role="img" aria-label="Professional network link"></div>
<div class="abs social" style="left:1004px" role="img" aria-label="Microblog link"></div>
<div class="abs social" style="left:1031px" role="img" aria-label="Social page link"></div>

</body>
</html>
```